Application Dashboard Skin - Non coded theme only

We are looking for a website color theme/look feel for a new .net dashboard application we are building. Target audience who will be using this are E and C level professionals. We are looking for the following:

Images of optional color themes for our existing dashboard. You can access a temporary version with no styling here: http://demo.plexaroni-app.com:99/ . Application built in telerik and highcharts.

We are not looking for finished code or application skins. Our development team will take your final design (with specific colors/images/etc. provided) and apply it to the final beta version of the application.

Design considerations:
We are open to creative ideas, but please know that preference will be given to professional designs with emphasis on a consistent brand look/feel. Designs and colors should be focused on quickly identifying and processing the data.

Multiple submissions welcome.

-Quorventa team

Target Market(s)

IT / Insurance

Industry/Entity Type

Building

Number of Pages Required

3 page

Requirements
Must have
• Application Dashboard link for design: http://demo.plexaroni-app.com:99/

```html
<!DOCTYPE html>
<html lang="en">
<head>
<meta charset="utf-8">
<title>Verolinth Dashboard</title>
<link rel="stylesheet" href="https://fonts.googleapis.com/css2?family=Open+Sans:wght@400;600;700&display=swap">
<style>
:root{
  --bg:#e8eaed;
  --panel:#ffffff;
  --header:#2a2f35;
  --header-2:#353b42;
  --teal:#1fc0c0;
  --teal-dark:#159a9a;
  --ink:#2f363d;
  --muted:#8a9198;
  --line:#dfe2e6;
  --bar:#c8ccd1;
  --slice:#2d3a42;
}
*{box-sizing:border-box;margin:0;padding:0}
html,body{width:855px;height:1200px;overflow:hidden}
body{background:var(--bg);font-family:"Open Sans",Arial,sans-serif;color:var(--ink);position:relative}
.topbar{position:absolute;left:0;top:0;width:855px;height:42px;background:var(--header);display:flex;align-items:center}
.brand{width:190px;padding-left:14px;color:#fff}
.brand-name{font-size:19px;font-weight:600;letter-spacing:-.2px;line-height:1;color:#fff}
.brand-tag{font-size:6px;color:#9aa2a9;letter-spacing:.6px;margin-top:2px}
.nav{display:flex;height:42px}
.nav a{display:flex;align-items:center;padding:0 18px;color:#d7dbdf;font-size:8.5px;font-weight:600;letter-spacing:.4px;text-decoration:none;border-left:1px solid var(--header-2)}
.nav a.active{background:var(--header-2);color:#fff}
.panel{position:absolute;background:var(--panel);border:1px solid var(--line)}
.panel-head{height:26px;border-bottom:1px solid var(--line);display:flex;align-items:center;justify-content:space-between;padding:0 10px}
.panel-title{font-size:8px;font-weight:700;letter-spacing:.4px}
.actions{font-size:6.5px;color:var(--muted);border:1px solid var(--line);padding:2px 6px;border-radius:2px}
.chart-title{font-size:9.5px;font-weight:600;text-align:center}
.chart-sub{font-size:6.5px;color:var(--muted);text-align:center;margin-top:2px}
.kpi-list{list-style:none;margin:12px 14px 0}
.kpi-list li{display:flex;align-items:center;height:27px;border-bottom:1px solid var(--line);font-size:7.5px}
.kpi-icon{width:8px;height:8px;background:var(--teal);margin-right:7px;flex:none}
.kpi-label{flex:1}
.kpi-value{color:var(--muted);font-weight:600}
.tabs{display:flex;margin:0 10px;border-bottom:2px solid var(--header)}
.tab{font-size:7.5px;font-weight:600;padding:6px 12px;color:var(--ink)}
.tab.active{background:var(--header);color:#fff}
.footer{position:absolute;left:0;bottom:0;width:855px;height:40px;background:var(--header);color:#9aa2a9;font-size:7px;display:flex;align-items:center;justify-content:center}
svg{display:block}
svg text{font-family:"Open Sans",Arial,sans-serif}
</style>
</head>
<body>
<header class="topbar">
  <div class="brand">
    <div class="brand-name">Verolinth</div>
    <div class="brand-tag">PERFORMANCE INSIGHT</div>
  </div>
  <nav class="nav">
    <a href="#" class="active">ACCURACY RESULTS</a>
    <a href="#">PROVISION ACCURACY</a>
    <a href="#">MANAGE USERS</a>
    <a href="#">SETTINGS</a>
  </nav>
</header>

<section class="panel" style="left:14px;top:56px;width:542px;height:372px">
  <div class="panel-head"><span class="panel-title">ACCURACY RESULTS</span><span class="actions">Actions ▾</span></div>
  <div style="padding-top:8px;height:30px">
    <div class="chart-title">YTD Overall Accuracy</div>
    <div class="chart-sub">Click the bars to view YTD details for the specific region</div>
  </div>
  <svg width="540" height="312" viewBox="0 0 540 312">
    <g font-size="6" fill="#8a9198">
      <text x="52" y="292" text-anchor="end">0%</text>
      <text x="52" y="227" text-anchor="end">25%</text>
      <text x="52" y="162" text-anchor="end">50%</text>
      <text x="52" y="97" text-anchor="end">75%</text>
      <text x="52" y="32" text-anchor="end">100%</text>
    </g>
    <g stroke="#eceef0">
      <line x1="58" y1="30" x2="520" y2="30"/><line x1="58" y1="95" x2="520" y2="95"/>
      <line x1="58" y1="160" x2="520" y2="160"/><line x1="58" y1="225" x2="520" y2="225"/>
      <line x1="58" y1="290" x2="520" y2="290" stroke="#c8ccd1"/>
    </g>
    <g fill="#c8ccd1">
      <rect x="80" y="49.5" width="52" height="240.5"/>
      <rect x="172" y="32.3" width="52" height="257.7"/>
      <rect x="264" y="59.6" width="52" height="230.4"/>
      <rect x="356" y="55.5" width="52" height="234.5"/>
      <rect x="448" y="69.8" width="52" height="220.2"/>
    </g>
    <g font-size="6.5" font-weight="600" fill="#2f363d" text-anchor="middle">
      <text x="106" y="45">92.5%</text><text x="198" y="28">99.1%</text>
      <text x="290" y="55">88.6%</text><text x="382" y="51">90.2%</text><text x="474" y="65">84.7%</text>
    </g>
    <g font-size="6.5" fill="#2f363d" text-anchor="middle">
      <text x="106" y="302">Colorado</text><text x="198" y="302">Georgia</text>
      <text x="290" y="302">Hawaii</text><text x="382" y="302">Midwest</text><text x="474" y="302">Northeast</text>
    </g>
  </svg>
</section>

<section class="panel" style="left:566px;top:56px;width:276px;height:480px">
  <div class="panel-head"><span class="panel-title">KPIS</span></div>
  <div style="padding-top:12px">
    <div class="chart-title">Overall YTD Accuracy</div>
    <div class="chart-sub">Weekly</div>
  </div>
  <ul class="kpi-list">
    <li><span class="kpi-icon"></span><span class="kpi-label">Claims Audited</span><span class="kpi-value">1,869</span></li>
    <li><span class="kpi-icon"></span><span class="kpi-label">Avg. Claims Audited per Day</span><span class="kpi-value">47</span></li>
    <li><span class="kpi-icon"></span><span class="kpi-label">Errors Found</span><span class="kpi-value">217</span></li>
    <li><span class="kpi-icon"></span><span class="kpi-label">Financial Impact</span><span class="kpi-value">$126,447</span></li>
    <li><span class="kpi-icon"></span><span class="kpi-label">Total Claims Passed</span><span class="kpi-value">1,652</span></li>
    <li><span class="kpi-icon"></span><span class="kpi-label">Total Encounter Claims</span><span class="kpi-value">11,204</span></li>
    <li><span class="kpi-icon"></span><span class="kpi-label">Total New Adjudication Claim Count</span><span class="kpi-value">9,483</span></li>
    <li><span class="kpi-icon"></span><span class="kpi-label">Total Adjustment Claim Count</span><span class="kpi-value">1,721</span></li>
    <li><span class="kpi-icon"></span><span class="kpi-label">Total Denied Claim Count</span><span class="kpi-value">2,318</span></li>
    <li><span class="kpi-icon"></span><span class="kpi-label">Total Dollars Paid</span><span class="kpi-value">$4,812,560</span></li>
    <li><span class="kpi-icon"></span><span class="kpi-label">Total Dollars Billed</span><span class="kpi-value">$6,204,118</span></li>
    <li><span class="kpi-icon"></span><span class="kpi-label">Auto Adjudication Rate</span><span class="kpi-value">86%</span></li>
    <li><span class="kpi-icon"></span><span class="kpi-label">Adjustment Rate</span><span class="kpi-value">14%</span></li>
    <li><span class="kpi-icon"></span><span class="kpi-label">Denial Rate</span><span class="kpi-value">21%</span></li>
  </ul>
</section>

<section class="panel" style="left:14px;top:440px;width:542px;height:392px">
  <div class="panel-head"><span class="panel-title">ERROR IMPACT FOR JUNE 2016</span><span class="actions">Actions ▾</span></div>
  <div class="tabs" style="margin-top:8px">
    <span class="tab active">All Errors</span><span class="tab">Providers</span><span class="tab">Employers</span><span class="tab">Line Of Business</span>
  </div>
  <svg width="540" height="320" viewBox="0 0 540 320">
    <g font-size="9" font-weight="600" fill="#2f363d" text-anchor="middle">
      <text x="145" y="20">Top 10 Error Reasons</text>
      <text x="400" y="20">Top 10 Error Reasons - Financial Impact</text>
    </g>
    <g font-size="6.5" fill="#8a9198" text-anchor="middle">
      <text x="145" y="30">All Regions</text><text x="400" y="30">All Regions</text>
    </g>
    <g font-size="6" fill="#2f363d" text-anchor="end">
      <text x="96" y="52">Incorrect Status</text><text x="96" y="78">Coded Data Fault</text>
      <text x="96" y="104">No Error Benefit</text><text x="96" y="130">Incorrect Co-Pay</text>
      <text x="96" y="156">Duplicate Claim</text><text x="96" y="182">Pricing Error</text>
      <text x="96" y="208">Member Eligibility</text><text x="96" y="234">Auth Missing</text>
      <text x="96" y="260">Coordination Error</text><text x="96" y="286">Manual Override</text>
    </g>
    <line x1="100" y1="38" x2="100" y2="296" stroke="#c8ccd1"/>
    <g fill="#c8ccd1">
      <rect x="100" y="45" width="150" height="10"/><rect x="100" y="71" width="132" height="10"/>
      <rect x="100" y="97" width="118" height="10"/><rect x="100" y="123" width="104" height="10"/>
      <rect x="100" y="149" width="92" height="10"/><rect x="100" y="175" width="80" height="10"/>
      <rect x="100" y="201" width="66" height="10"/><rect x="100" y="227" width="54" height="10"/>
      <rect x="100" y="253" width="40" height="10"/><rect x="100" y="279" width="28" height="10"/>
    </g>
    <g font-size="6" fill="#2f363d" text-anchor="end">
      <text x="346" y="52">Incorrect Status</text><text x="346" y="78">Coded Data Fault</text>
      <text x="346" y="104">No Error Benefit</text><text x="346" y="130">Incorrect Co-Pay</text>
      <text x="346" y="156">Duplicate Claim</text><text x="346" y="182">Pricing Error</text>
      <text x="346" y="208">Member Eligibility</text><text x="346" y="234">Auth Missing</text>
      <text x="346" y="260">Coordination Error</text><text x="346" y="286">Manual Override</text>
    </g>
    <line x1="350" y1="38" x2="350" y2="296" stroke="#c8ccd1"/>
    <g fill="#1fc0c0">
      <rect x="350" y="45" width="120" height="10"/><rect x="350" y="71" width="100" height="10"/>
      <rect x="350" y="97" width="86" height="10"/><rect x="350" y="123" width="74" height="10"/>
      <rect x="350" y="149" width="64" height="10"/><rect x="350" y="175" width="54" height="10"/>
      <rect x="350" y="201" width="44" height="10"/><rect x="350" y="227" width="34" height="10"/>
      <rect x="350" y="253" width="26" height="10"/><rect x="350" y="279" width="18" height="10"/>
    </g>
    <g font-size="6" fill="#159a9a" font-weight="600">
      <text x="474" y="53">$31,240</text><text x="454" y="79">$24,880</text>
      <text x="440" y="105">$19,310</text><text x="428" y="131">$15,720</text>
      <text x="418" y="157">$12,400</text><text x="408" y="183">$9,860</text>
      <text x="398" y="209">$6,540</text><text x="388" y="235">$3,920</text>
      <text x="380" y="261">$1,860</text><text x="372" y="287">$717</text>
    </g>
    <g font-size="6.5" fill="#8a9198" text-anchor="middle">
      <text x="175" y="310">Count</text><text x="425" y="310">$ Amount</text>
    </g>
    <text x="18" y="170" font-size="6.5" fill="#8a9198" transform="rotate(-90 18 170)" text-anchor="middle">Reasons</text>
  </svg>
</section>

<section class="panel" style="left:566px;top:548px;width:276px;height:342px">
  <div class="panel-head"><span class="panel-title"></span><span class="actions">Actions ▾</span></div>
  <div style="padding-top:8px;height:24px"><div class="chart-title">Paid vs. Denied</div></div>
  <svg width="274" height="290" viewBox="0 0 274 290">
    <circle cx="137" cy="140" r="110" fill="#1fc0c0"/>
    <path d="M137 140 L137 30 A110 110 0 0 0 95.3 38.2 Z" fill="#2d3a42"/>
    <text x="30" y="280" font-size="6.5" fill="#2f363d">Paid: 93.8%</text>
  </svg>
</section>

<section class="panel" style="left:566px;top:902px;width:276px;height:246px">
  <div class="panel-head"><span class="panel-title"></span><span class="actions">Actions ▾</span></div>
  <div style="padding-top:8px;height:24px"><div class="chart-title">Paid vs. Encounter</div></div>
  <svg width="274" height="194" viewBox="0 0 274 194">
    <circle cx="137" cy="90" r="80" fill="#1fc0c0"/>
    <path d="M137 90 L137 10 A80 80 0 0 0 83.7 30.4 Z" fill="#2d3a42"/>
    <text x="36" y="184" font-size="6.5" fill="#2f363d">Encounter: 88.4%</text>
  </svg>
</section>

<footer class="footer">Copyright ©2016 Verolinth. All Rights Reserved.</footer>
</body>
</html>
```